Freelancers in the field of IT security and IT service need a business card design

I need a business card design for my company. I am a freelancer and active in the area of IT security, IT support% 26 # 252; tung, consulting. I am not yet color-coded, but it should be a modern color that can also be used for a later website. The design should be innovation. Exude dynamism and reliability

Target Market(s)

IT security, IT solutions

Contact Information for Business Card

Firma: brunov-consulting, Inhaber: Lukas Brunov
Adresse: Lindenhof 4, D-73618 Talheimstett
Telefon: +49 (0) 5137 640928
E-Mail Lukas.Brunov@brunov-consulting.example

```html
<!DOCTYPE html>
<html lang="de">
<head>
<meta charset="utf-8">
<title>Brunov Consulting – Visitenkarte</title>
<link rel="stylesheet" href="https://fonts.googleapis.com/css2?family=Montserrat:wght@300;400;500;700&display=swap">
<style>
  :root {
    --stage: #232323;
    --card-dark: #141414;
    --card-light: #ffffff;
    --brand-blue: #1aa3e8;
    --text-grey: #8e8e8e;
    --text-dark: #2b2b2b;
    --rule: #9a9a9a;
  }
  * { box-sizing: border-box; margin: 0; padding: 0; }
  html, body {
    width: 1200px; height: 852px; overflow: hidden;
    background: var(--stage);
    font-family: "Montserrat", Arial, sans-serif;
  }
  .stage {
    position: relative; width: 1200px; height: 852px;
    display: flex; align-items: center; justify-content: center; gap: 40px;
  }
  .card {
    position: relative; width: 540px; height: 310px;
    border-radius: 18px; overflow: hidden;
  }
  .card--back { background: var(--card-dark); border: 1px solid #2e2e2e; }
  .card--front { background: var(--card-light); }

  .wordmark {
    color: var(--brand-blue); font-weight: 400; line-height: 1;
    text-transform: uppercase;
  }
  .wordmark__line { display: block; }

  .card--back .wordmark {
    position: absolute; left: 0; right: 0; top: 96px; text-align: center;
  }
  .card--back .wordmark__line--main { font-size: 72px; letter-spacing: 4px; }
  .card--back .wordmark__line--sub { font-size: 30px; letter-spacing: 9px; margin-top: 8px; }

  .card--front .wordmark {
    position: absolute; right: 40px; top: 34px; text-align: right;
  }
  .card--front .wordmark__line--main { font-size: 36px; letter-spacing: 2px; }
  .card--front .wordmark__line--sub { font-size: 15px; letter-spacing: 4.6px; margin-top: 4px; }

  .rule { position: absolute; height: 1px; background: var(--rule); }
  .rule--upper { left: 250px; right: 40px; top: 140px; }
  .rule--lower { left: 40px; right: 40px; top: 258px; }

  .holder { position: absolute; left: 40px; top: 170px; }
  .holder__name {
    color: var(--brand-blue); font-weight: 700; font-size: 19px;
    letter-spacing: 0.5px; text-transform: uppercase;
  }
  .holder__role { color: var(--text-grey); font-size: 13px; margin-top: 3px; }

  .address {
    position: absolute; left: 40px; top: 230px;
    color: var(--text-dark); font-size: 12.5px;
  }
  .contact {
    position: absolute; left: 40px; right: 40px; top: 270px;
    color: var(--text-dark); font-size: 12.5px; white-space: nowrap;
  }
  .contact__label { color: var(--brand-blue); font-weight: 500; }
  .contact__sep { color: var(--text-grey); margin: 0 5px; }
</style>
</head>
<body>
<main class="stage">
  <section class="card card--back" aria-label="Kartenrückseite">
    <div class="wordmark">
      <span class="wordmark__line wordmark__line--main">Brunov</span>
      <span class="wordmark__line wordmark__line--sub">Consulting</span>
    </div>
  </section>

  <section class="card card--front" aria-label="Kartenvorderseite">
    <div class="wordmark">
      <span class="wordmark__line wordmark__line--main">Brunov</span>
      <span class="wordmark__line wordmark__line--sub">Consulting</span>
    </div>
    <div class="rule rule--upper"></div>
    <div class="holder">
      <p class="holder__name">Lukas Brunov</p>
      <p class="holder__role">Inhaber</p>
    </div>
    <p class="address">Lindenhof 4, D-73618 Talheimstett</p>
    <div class="rule rule--lower"></div>
    <p class="contact">
      <span class="contact__label">P:</span> +49 (0) 5137 640928<span class="contact__sep">|</span><span class="contact__label">E:</span> Lukas.Brunov@brunov-consulting.example
    </p>
  </section>
</main>
</body>
</html>
```